Web design for sitter site

We will be launching a sitter site in the coming months that focuses on sitters for children. The name of this site will be KidHaven.com
We will need:
1. main page design
2. site logo designed
3. subpages as well for the look of people's profiles, and job listings, etc (see links below)
We only need the design, photos, font files, etc. We do not need this site coded (no html), a ps job is fine.
Some competing sites in the space include - tendlyhub.com and vurl.com
http://www.brisk-minder.example/images/profile1.jpg
http://quenthollibrary.example/wp-content/uploads/2013/09/vurl-review.png
http://www.palvermont.example/hr/photos/tendly_hub2.jpg
Target Market(s)
Mothers of children, mainly women
Industry/Entity Type
Online
Look and feel

```html
<!DOCTYPE html>
<html lang="en">
<head>
<meta charset="utf-8">
<title>KidHaven – Find local babysitters</title>
<link href="https://fonts.googleapis.com/css2?family=Signika:wght@300;400;600&family=Open+Sans:ital,wght@0,400;0,600;1,700&display=swap" rel="stylesheet">
<style>
:root{
  --green:#7cb518;
  --green-panel:#c8df94;
  --yellow-panel:#f5dc86;
  --orange:#f2b705;
  --page:#efeee9;
  --footer:#e3e2df;
  --white:#ffffff;
  --text:#3d3d3d;
  --teal:#6fa8a6;
  --line:#dcdcd8;
}
*{box-sizing:border-box;margin:0;padding:0}
html,body{width:1043px;height:1200px;overflow:hidden}
body{position:relative;background:var(--page);font-family:'Open Sans',sans-serif;color:var(--text)}
.abs{position:absolute}
.stripe{position:absolute;left:0;width:1043px;height:7px;display:flex}
.stripe span{flex:1}
.stripe.bottom{top:1190px;height:10px}
.header{top:7px;left:0;width:1043px;height:68px;background:var(--white);border-bottom:1px solid #e4e4e4}
.logo{left:108px;top:16px;display:flex;align-items:center;gap:6px;font-family:'Signika',sans-serif;font-weight:300;font-size:34px;color:var(--green);line-height:1}
.logo i{width:26px;height:26px;border:2px solid var(--green);border-radius:50%}
.nav-link{top:28px;left:436px;font-family:'Signika',sans-serif;font-weight:600;font-size:12.5px;color:#333}
.nav-btn{top:25px;height:33px;border:1.5px dashed #d8d8d8;border-radius:5px;font-family:'Signika',sans-serif;font-weight:600;font-size:12.5px;display:flex;align-items:center;justify-content:center}
.nav-btn.parents{left:566px;width:136px;color:var(--green)}
.nav-btn.sitter{left:709px;width:118px;color:#9a9a9a}
.nav-arrow{left:839px;top:35px;width:0;height:0;border-left:8px solid #b5b5b5;border-top:5px solid transparent;border-bottom:5px solid transparent}
.login{left:860px;top:22px;width:76px;height:34px;background:var(--green);color:#fff;font-family:'Signika',sans-serif;font-weight:600;font-size:16px;display:flex;align-items:center;justify-content:center}
.hero{top:75px;left:0;width:1043px;height:351px;background:#f3f3f1}
.hero-photo{left:426px;top:75px;width:617px;height:351px;background:linear-gradient(120deg,#fbf7f3 0%,#f6e3d5 45%,#f9eee6 70%,#fdfbf9 100%)}
.panel{left:107px;width:319px;padding:14px}
.panel.sitters{top:75px;height:170px;background:var(--green-panel)}
.panel.parents{top:255px;height:171px;background:var(--yellow-panel)}
.panel h2{font-family:'Signika',sans-serif;font-weight:300;font-size:16px;line-height:1.1;color:#333;margin-bottom:10px}
.ticks{display:grid;grid-template-columns:1fr 1fr;column-gap:8px;row-gap:10px;list-style:none}
.ticks li{display:flex;gap:6px;font-size:10px;line-height:1.3;color:#555}
.ticks li::before{content:"";flex:none;width:9px;height:9px;border:1.5px solid var(--green);border-radius:50%;margin-top:1px}
.become{left:173px;top:193px;width:188px;height:44px;background:var(--orange);border:2px solid #f6cf55;color:#fff;font-family:'Signika',sans-serif;font-weight:600;font-size:12px;display:flex;align-items:center;justify-content:center}
.zip{left:125px;top:383px;width:133px;height:36px;background:#fff;border:1px solid #ccc;font-size:9px;color:#666;padding:12px 11px}
.find{left:274px;top:383px;width:133px;height:36px;background:var(--green);color:#fff;font-family:'Signika',sans-serif;font-weight:600;font-size:11.5px;display:flex;align-items:center;justify-content:center}
.tab{top:489px;height:31px;font-family:'Signika',sans-serif;font-weight:300;font-size:13.5px;display:flex;align-items:center;justify-content:center}
.tab.new{left:107px;width:147px;background:#f7f7f5;border:1px solid var(--line);border-bottom:none;color:#444}
.tab.featured{left:258px;width:160px;background:var(--green);color:#fff;font-weight:400;border:2px solid #a5d05a;border-bottom:none}
.board{left:106px;top:519px;width:831px;height:386px;background:var(--white);border:1px solid var(--line)}
.card{top:541px;width:178px}
.card .photo{width:178px;height:145px;border:2px solid #e2e2e2}
.card .row{display:flex;align-items:center;gap:7px;margin-left:4px}
.card .name{margin-top:16px;font-family:'Signika',sans-serif;font-weight:300;font-size:12.5px;color:#333}
.card .meta{margin-top:6px;font-size:9px;color:#777}
.card p{margin:6px 0 0 8px;width:160px;font-size:10px;line-height:1.25;color:#999}
.view{position:absolute;top:302px;width:116px;height:33px;background:var(--green);border:2px solid #a5d05a;color:#fff;font-weight:700;font-style:italic;font-size:10px;display:flex;align-items:center;justify-content:center}
.divider{top:541px;width:1px;height:333px;background:#eee}
.footer{top:960px;left:0;width:1043px;height:230px;background:var(--footer)}
.box{background:#f3f2ef}
.about{left:106px;top:974px;width:269px;height:175px;padding:16px 23px}
.about h3,.newsletter h3,.social h3{font-family:'Signika',sans-serif;font-weight:400;font-size:14px;color:#333}
.about p{margin-top:12px;font-size:10.5px;line-height:1.45;color:#777}
.contact{left:388px;top:974px;width:265px;height:76px;padding:14px 12px}
.contact .line{display:flex;align-items:center;gap:10px;font-size:11.5px;color:#333;height:22px;white-space:nowrap}
.contact .line+.line{margin-top:8px}
.ring{width:22px;height:22px;border:1.5px solid #ccc;border-radius:50%;flex:none}
.newsletter{left:675px;top:974px;width:261px;height:76px;padding:14px 8px 14px 12px}
.newsletter ul{list-style:none;margin-top:8px;display:grid;grid-template-columns:132px auto;row-gap:8px}
.newsletter li{font-size:9px;color:#666;display:flex;align-items:center;gap:5px;white-space:nowrap}
.newsletter li::before{content:"";width:7px;height:7px;border-radius:50%;background:var(--green);flex:none}
.social{left:388px;top:1065px;width:543px;height:84px;padding:12px 21px}
.social .subscribe-title{position:absolute;left:252px;top:12px}
.icons{display:flex;gap:9px;margin-top:20px}
.icons span{width:23px;height:23px;border:1.5px solid #c8c8c8;border-radius:50%}
.email{position:absolute;left:249px;top:38px;width:202px;height:34px;border:1.5px solid #ccc;border-radius:8px;background:#fff;font-size:9.5px;color:#999;padding:10px 15px}
.send{position:absolute;left:463px;top:38px;width:72px;height:34px;background:var(--green);border:2px solid #a5d05a;border-radius:8px;color:#fff;font-family:'Signika',sans-serif;font-weight:600;font-size:14px;display:flex;align-items:center;justify-content:center}
.bottom-links{left:108px;top:1162px;font-size:10px;color:#555;display:flex;gap:6px}
.copyright{right:117px;top:1162px;font-size:10px;color:#555}
</style>
</head>
<body>

<div class="stripe" style="top:0">
  <span style="background:#7fbfbf"></span><span style="background:#c9c6c0"></span><span style="background:#e47f86"></span><span style="background:#5f85b4"></span><span style="background:#4ed6df"></span><span style="background:#f2cf4b"></span><span style="background:#8cbcb7"></span><span style="background:#dcb4b6"></span><span style="background:#c9c6c0"></span><span style="background:#d9e07a"></span><span style="background:#c9c6c0"></span>
</div>

<header class="abs header">
  <div class="abs logo"><i></i>KidHaven</div>
  <div class="abs nav-link">Trust &amp; Safety Center</div>
  <div class="abs nav-btn parents">Sign Up For Parents</div>
  <div class="abs nav-btn sitter">Signup for Sitter</div>
  <div class="abs nav-arrow"></div>
  <div class="abs login">Login</div>
</header>

<section class="abs hero"></section>
<div class="abs hero-photo" role="img" aria-label="Photo of three babies sitting and playing with colourful toys"></div>

<div class="abs panel sitters">
  <h2>Find local babysitters with:</h2>
  <ul class="ticks">
    <li>CPR and first aid training</li>
    <li>Background checks</li>
    <li>Age-specific skills and experience</li>
    <li>Household skills like cooking &amp; cleaning</li>
  </ul>
</div>
<div class="abs become">BECOME A BABY SITTER</div>

<div class="abs panel parents">
  <h2>Find experienced babysitters in your neighborhood</h2>
  <ul class="ticks">
    <li>Full-time and part-time nannies</li>
    <li>Before after-school care</li>
    <li>Regular babysitters</li>
    <li>Overnight care</li>
  </ul>
</div>
<div class="abs zip">Search by zip code....</div>
<div class="abs find">FIND FOR FREE</div>

<div class="abs tab new">New Babysitters</div>
<div class="abs tab featured">Featured Babysitters</div>
<div class="abs board"></div>

<div class="abs divider" style="left:311px"></div>
<div class="abs divider" style="left:517px"></div>
<div class="abs divider" style="left:724px"></div>

<article class="abs card" style="left:120px">
  <div class="photo" role="img" aria-label="Portrait photo of babysitter Elizabeth" style="background:linear-gradient(160deg,#8a8f96,#c9a48e 50%,#5a3d30)"></div>
  <div class="row name"><svg width="11" height="11" viewBox="0 0 12 12"><circle cx="6" cy="3.5" r="2.8" fill="#6fa8a6"/><path d="M1 12c0-4 2.2-5.5 5-5.5S11 8 11 12z" fill="#6fa8a6"/></svg>Elizabeth G.</div>
  <div class="row meta"><svg width="10" height="12" viewBox="0 0 10 12"><path d="M5 0a4 4 0 0 0-4 4c0 3 4 8 4 8s4-5 4-8a4 4 0 0 0-4-4z" fill="#6fa8a6"/><circle cx="5" cy="4" r="1.5" fill="#fff"/></svg>San Diego, CA</div>
  <div class="row meta"><b style="color:#6fa8a6;font-size:11px;width:10px">$</b>10-15</div>
  <p>Lorem Ipsum is simply dummy text of the printing and typeset-ting industry. Lorem Ipsum has been the industry's standard dummy text ever since</p>
  <div class="view" style="left:18px">View Profile</div>
</article>

<article class="abs card" style="left:326px">
  <div class="photo" role="img" aria-label="Photo of a sitter and a girl wearing sunglasses" style="background:linear-gradient(160deg,#6d6f62,#c6566f 55%,#3b3a3c)"></div>
  <div class="row name"><svg width="11" height="11" viewBox="0 0 12 12"><circle cx="6" cy="3.5" r="2.8" fill="#6fa8a6"/><path d="M1 12c0-4 2.2-5.5 5-5.5S11 8 11 12z" fill="#6fa8a6"/></svg>Jessica N.</div>
  <div class="row meta"><svg width="10" height="12" viewBox="0 0 10 12"><path d="M5 0a4 4 0 0 0-4 4c0 3 4 8 4 8s4-5 4-8a4 4 0 0 0-4-4z" fill="#6fa8a6"/><circle cx="5" cy="4" r="1.5" fill="#fff"/></svg>Gloucester, MA</div>
  <div class="row meta"><b style="color:#6fa8a6;font-size:11px;width:10px">$</b>10-20</div>
  <p>Lorem Ipsum is simply dummy text of the printing and typeset-ting industry. Lorem Ipsum has been the industry's standard dummy text ever since</p>
  <div class="view" style="left:40px">View Profile</div>
</article>

<article class="abs card" style="left:532px">
  <div class="photo" role="img" aria-label="Photo of a sitter and a girl looking at a phone" style="background:linear-gradient(160deg,#9a6a4e,#d9a08a 45%,#6fc7a8 75%,#e06d9a)"></div>
  <div class="row name"><svg width="11" height="11" viewBox="0 0 12 12"><circle cx="6" cy="3.5" r="2.8" fill="#6fa8a6"/><path d="M1 12c0-4 2.2-5.5 5-5.5S11 8 11 12z" fill="#6fa8a6"/></svg>Jessica N.</div>
  <div class="row meta"><svg width="10" height="12" viewBox="0 0 10 12"><path d="M5 0a4 4 0 0 0-4 4c0 3 4 8 4 8s4-5 4-8a4 4 0 0 0-4-4z" fill="#6fa8a6"/><circle cx="5" cy="4" r="1.5" fill="#fff"/></svg>Diamond Bar, CA</div>
  <div class="row meta"><b style="color:#6fa8a6;font-size:11px;width:10px">$</b>10-25</div>
  <p>Lorem Ipsum is simply dummy text of the printing and typeset-ting industry. Lorem Ipsum has been the industry's standard dummy text ever since</p>
  <div class="view" style="left:40px">View Profile</div>
</article>

<article class="abs card" style="left:739px">
  <div class="photo" role="img" aria-label="Photo of a sitter baking with two boys in a kitchen" style="background:linear-gradient(160deg,#d9d6cf,#b9a58c 45%,#3f3a36 70%,#d8c9b0)"></div>
  <div class="row name"><svg width="11" height="11" viewBox="0 0 12 12"><circle cx="6" cy="3.5" r="2.8" fill="#6fa8a6"/><path d="M1 12c0-4 2.2-5.5 5-5.5S11 8 11 12z" fill="#6fa8a6"/></svg>Stephanie F.</div>
  <div class="row meta"><svg width="10" height="12" viewBox="0 0 10 12"><path d="M5 0a4 4 0 0 0-4 4c0 3 4 8 4 8s4-5 4-8a4 4 0 0 0-4-4z" fill="#6fa8a6"/><circle cx="5" cy="4" r="1.5" fill="#fff"/></svg>San Diego, CA</div>
  <div class="row meta"><b style="color:#6fa8a6;font-size:11px;width:10px">$</b>10-15</div>
  <p>Lorem Ipsum is simply dummy text of the printing and typeset-ting industry. Lorem Ipsum has been the industry's standard dummy text ever since</p>
  <div class="view" style="left:34px">View Profile</div>
</article>

<footer class="abs footer"></footer>

<div class="abs box about">
  <h3>About KidHaven</h3>
  <p>Lorem Ipsum is simply dummy text of the printing and typesetting industry. Lorem Ipsum has been the industry's standard dummy text ever since the 1500s, when an unknown printer took a galley of type and scrambled it to make a type specimen book.</p>
</div>

<div class="abs box contact">
  <div class="line"><span class="ring"></span>555-204-318-462 or 555-2047-318-906</div>
  <div class="line"><span class="ring"></span>info@KidHaven.com</div>
</div>

<div class="abs box newsletter">
  <h3>Newsletter</h3>
  <ul>
    <li>Parents: Post Your Job</li>
    <li>Caregivers: Apply Jobs</li>
    <li>Find the Right Match</li>
  </ul>
</div>

<div class="abs box social">
  <h3>Get Social With Us</h3>
  <h3 class="subscribe-title">Subscribe &nbsp;With Us!</h3>
  <div class="icons"><span></span><span></span><span></span><span></span><span></span><span></span></div>
  <div class="email">Your Email.........</div>
  <div class="send">Send</div>
</div>

<nav class="abs bottom-links">
  <span>Home</span><span>-</span><span>About us -</span><span>Privacy Policy</span><span>-</span><span>Terms &amp; Condition</span><span>-</span><span>Contact us</span>
</nav>
<div class="abs copyright">© 2014 Copyright &nbsp;All Rights Reserved KidHaven.com</div>

<div class="stripe bottom">
  <span style="background:#7fbfbf"></span><span style="background:#c9c6c0"></span><span style="background:#e47f86"></span><span style="background:#5f85b4"></span><span style="background:#4ed6df"></span><span style="background:#f2cf4b"></span><span style="background:#8cbcb7"></span><span style="background:#dcb4b6"></span><span style="background:#c9c6c0"></span><span style="background:#d9e07a"></span><span style="background:#c9c6c0"></span>
</div>

</body>
</html>
```